Help Liu Wenhao redesign his business card!

Liu Wenhao, an "influential" Chinese businessman, made international headlines this week with his business card...but not for the right reasons. Help Liu Wenhao redesign his new business card - funny and/or satirical submissions welcome!

Check out his hilarious business card that he was giving out on a trip to New York, with not one, not two...but TEN titles! Let's just say they're not the most humble titles either :).

Read more about Liu's business card here: http://blogs.brightledger.example/asiadesk/2014/01/14/liu-wenhaos-business-card-needs-to-be-recycled/

While the rest of the world is laughing at him, we want to help. This is an unofficial contest, but we'd like the PixelForge community to have a shot at redesigning Liu's business card. Thousands of businesses have used PixelForge.example to create beautiful business cards, so we know the community of designers here can do a great job.

We'd like you to create a business card worthy of this honorable businessman, while also keeping a clean, dignified design.

Funny / satirical job titles and designs are encouraged. Note you do not have to use all of Liu's titles on the card. Feel free to come up with your own creative titles!

In regard to contact details, please use dummy contact details. Liu's company name and street address are:

China Tai-Mo Reusable Scrap & Restoration Corporation
Fuxing Road 7, Lanqiao District, Nanjing, China

You can design a single sided or double-sided card - it's completely up to you!

Target Market(s)

Business people and government officials of the world

Industry/Entity Type

Business

Font styles to use
Serif
Sans Serif
Decorative

Colors
ec2027
ffc214
6b449b
0455a3

Requirements
Must have
• At least 1 title, preferably more than 1.

Designers can approach this task how they like however one option could be to use one of Liu's titles and create a suitable business card graphic to suit the role. Designers are also encouraged to o make up a new title and design a graphic to suit.

Here are the titles - but you can also make up your own!

Most influential person of China
Most prominent Philanthropist of China
China Moral Leader
China Earthquake Rescue Hero
Most well-known and Beloved Chinese Role Model
China Top Ten Most Honorable Volunteer
Most Charismatic Philanthropist of China
China Low Carbon Emission
Environmental Protection Top Advocate
China's Foremost Environmental Preservation Demolition Expert
Should not have
• No black borders around photographs of Liu Wenhao
Do not present Liu Wenhao's image in grayscale (black and white)

For a detailed guideline for colors to avoid in design targeting the Chinese market, see http://www.corvalegroup.example/2011/01/17/color/

```html
<!DOCTYPE html>
<html lang="en">
<head>
<meta charset="utf-8">
<title>Wenhao Liu – Business Card</title>
<link href="https://fonts.googleapis.com/css2?family=Cinzel:wght@400;600&display=swap" rel="stylesheet">
<style>
  :root {
    --backdrop: #e6e6e4;
    --card-black: #0c0c0c;
    --card-black-light: #1c1c1c;
    --ink-white: #f4f4f4;
    --ink-soft: #cfcfcf;
    --rule: #bdbdbd;
    --photo-warm: #7a6450;
    --photo-deep: #3b2e25;
    --edge: #050505;
  }
  * { box-sizing: border-box; margin: 0; padding: 0; }
  html, body {
    width: 1200px; height: 900px; overflow: hidden;
    background: var(--backdrop);
    font-family: "Cinzel", "Times New Roman", serif;
  }
  .canvas {
    width: 1200px; height: 900px;
    display: flex; flex-direction: column;
    align-items: center; justify-content: center; gap: 40px;
  }
  .card {
    width: 680px; height: 388px;
    background: linear-gradient(135deg, var(--card-black-light), var(--card-black) 60%);
    color: var(--ink-white);
    position: relative; overflow: hidden;
    box-shadow: 0 10px 24px rgba(0,0,0,0.25);
  }
  /* Front */
  .card-front { display: flex; }
  .front-edge { width: 14px; background: var(--edge); }
  .portrait {
    width: 250px; height: 100%;
    background: linear-gradient(160deg, var(--photo-warm), var(--photo-deep));
  }
  .identity {
    flex: 1; position: relative;
    display: flex; flex-direction: column; align-items: center;
    padding-top: 26px;
  }
  .dot { width: 7px; height: 7px; border-radius: 50%; background: var(--ink-white); }
  .name {
    margin-top: 14px;
    font-size: 30px; font-weight: 600; letter-spacing: 1px;
  }
  .name-rule {
    width: 300px; height: 1px; background: var(--rule); margin-top: 6px;
  }
  .role { margin-top: 8px; font-size: 15px; letter-spacing: 1px; color: var(--ink-soft); }
  .company {
    position: absolute; right: 20px; bottom: 34px;
    text-align: right; font-size: 10.5px; line-height: 1.5;
    letter-spacing: 0.3px; color: var(--ink-soft);
  }
  /* Back */
  .card-back {
    display: flex; flex-direction: column; align-items: center;
    padding-top: 30px;
  }
  .titles {
    list-style: none; text-align: center;
    margin: 14px 0 12px;
    font-size: 17px; line-height: 1.55; letter-spacing: 0.4px;
  }
  .title-final { margin-top: 12px; font-size: 17px; letter-spacing: 0.4px; }
</style>
</head>
<body>
<main class="canvas">
  <section class="card card-front" aria-label="Card front">
    <div class="front-edge"></div>
    <div class="portrait" role="img" aria-label="Portrait photograph of Wenhao Liu in a dark suit, seated beside a carved wooden chair"></div>
    <div class="identity">
      <span class="dot"></span>
      <h1 class="name">Wenhao Liu</h1>
      <div class="name-rule"></div>
      <p class="role">CEO</p>
      <address class="company">
        China Tai-Mo Reusable Scrap &amp; Restoration Corporation<br>
        Fuxing Road 7, Lanqiao District, Nanjing, China
      </address>
    </div>
  </section>

  <section class="card card-back" aria-label="Card back">
    <span class="dot"></span>
    <ul class="titles">
      <li>Most influential person of China</li>
      <li>Most prominent Philanthropist of China</li>
      <li>China Moral Leader</li>
      <li>China Earthquake Rescue Hero</li>
      <li>Most well-known and Beloved Chinese Role Model</li>
      <li>China Top Ten Most Honorable Volunteer</li>
      <li>Most Charismatic Philanthropist of China</li>
      <li>China Low Carbon Emission</li>
      <li>Environmental Protection Top Advocate</li>
    </ul>
    <span class="dot"></span>
    <p class="title-final">China’s Foremost Environmental Preservation Demolition Expert</p>
  </section>
</main>
</body>
</html>
```